Business cards and logo for a international shipping company called Harborline Freight LLC. We would like to incorporate the colors red and blue. We would like the theme to be nautical.

Industry/Entity Type

Business

```html
<!DOCTYPE html>
<html lang="en">
<head>
<meta charset="UTF-8">
<title>Harborline Freight LLC – Business Cards</title>
<link rel="stylesheet" href="https://fonts.googleapis.com/css2?family=Montserrat:wght@600&family=Open+Sans:wght@400;600&display=swap">
<style>
  :root {
    --backdrop: #3a3a3c;
    --card-dark: #1b1b1c;
    --card-light: #f4f4f4;
    --brand-blue: #3a78c4;
    --brand-red: #d92d2d;
    --rule-red: #b3141f;
    --ink: #2b2b2b;
  }
  * { box-sizing: border-box; margin: 0; padding: 0; }
  html, body { width: 1200px; height: 900px; overflow: hidden; }
  body {
    background: var(--backdrop);
    font-family: "Open Sans", sans-serif;
    position: relative;
  }
  .card {
    position: absolute;
    left: 290px;
    width: 620px;
    height: 354px;
    border-radius: 22px;
  }
  .card--back { top: 48px; background: var(--card-dark); }
  .card--front { top: 446px; background: var(--card-light); overflow: hidden; }

  .brand {
    position: absolute;
    display: flex;
    align-items: center;
    gap: 12px;
    font-family: "Montserrat", sans-serif;
    font-weight: 600;
    color: var(--brand-blue);
    letter-spacing: 1px;
    white-space: nowrap;
  }
  .brand__mark { background: var(--brand-red); flex: none; }
  .card--back .brand {
    left: 50%; top: 50%;
    transform: translate(-50%, -50%);
    font-size: 34px;
  }
  .card--back .brand__mark { width: 22px; height: 22px; }
  .card--front .brand {
    right: 34px; top: 40px;
    font-size: 20px;
  }
  .card--front .brand__mark { width: 14px; height: 14px; }

  .identity {
    position: absolute;
    left: 34px; top: 112px;
    padding-left: 14px;
    border-left: 9px solid var(--rule-red);
  }
  .identity__name { font-size: 22px; color: var(--ink); line-height: 1.1; letter-spacing: -0.5px; }
  .identity__title { font-size: 15px; color: var(--rule-red); line-height: 1.3; }

  .contact {
    position: absolute;
    left: 34px; top: 218px;
    list-style: none;
  }
  .contact__item {
    display: flex; align-items: center; gap: 10px;
    font-size: 16px; color: var(--ink);
    height: 27px;
  }
  .contact__icon { width: 16px; height: 16px; flex: none; fill: var(--brand-blue); }

  .divider {
    position: absolute;
    left: 270px; right: 0; top: 306px;
    height: 2px; background: var(--rule-red);
  }
  .social {
    position: absolute;
    right: 34px; top: 268px;
    display: flex; align-items: center; gap: 8px;
    font-size: 16px; color: var(--ink);
  }
  .social__mark { width: 16px; height: 16px; background: var(--brand-red); }
</style>
</head>
<body>

<section class="card card--back">
  <div class="brand"><span class="brand__mark"></span>HARBORLINE FREIGHT</div>
</section>

<section class="card card--front">
  <div class="brand"><span class="brand__mark"></span>HARBORLINE FREIGHT</div>

  <div class="identity">
    <p class="identity__name">Your Name</p>
    <p class="identity__title">Job Title</p>
  </div>

  <ul class="contact">
    <li class="contact__item">
      <svg class="contact__icon" viewBox="0 0 16 16"><path d="M1 3h14v10H1z M1 3l7 6 7-6" fill="none" stroke="var(--brand-blue)" stroke-width="1.6"/></svg>
      youremail@harborline.test
    </li>
    <li class="contact__item">
      <svg class="contact__icon" viewBox="0 0 16 16"><path d="M3 1l3 3-2 2c1 2 3 4 6 6l2-2 3 3-2 2C7 15 1 9 1 3z"/></svg>
      000 000 0000
    </li>
    <li class="contact__item">
      <svg class="contact__icon" viewBox="0 0 16 16"><rect x="4" y="1" width="8" height="14" rx="1.5" fill="none" stroke="var(--brand-blue)" stroke-width="1.6"/><circle cx="8" cy="12.5" r="0.9"/></svg>
      000 000 0000
    </li>
    <li class="contact__item">
      <svg class="contact__icon" viewBox="0 0 16 16"><path d="M8 15C4 10 3 8 3 6a5 5 0 0 1 10 0c0 2-1 4-5 9z"/><circle cx="8" cy="6" r="1.8" fill="var(--card-light)"/></svg>
      your address
    </li>
  </ul>

  <div class="divider"></div>

  <div class="social"><span class="social__mark"></span>/harborlinefreight</div>
</section>

</body>
</html>
```